Looking for a creative label design for our retail coffee bags

We are a coffee manufacturer (coffee roaster) looking to re-brand our retail label for our coffee bags. Our main coffee blend that we sell is our Harborline Velvet Blend. You can use this name when creating the label. We are going for a look that represents our company as a coffee roaster. Please reference our website (www.brindlemugworks.com) and our Facebook page to learn more about our company and to give you more inspiration on creating this design.

Target Market(s)

Retail customers/grocery stores

Industry/Entity Type

Manufacturer

Requirements
Must have
• The size of the label has to be 3" width x 4" height

Logo must be Black
Nice to have
• We currently incorporate a color on our labels for each blend. For example, Harborline Velvet Blend (royal blue), Decaffeinated Blend (red), Breakfast Blend (green), Flavored coffees (gold).

Rustic/vintage style

```html
<!DOCTYPE html>
<html lang="en">
<head>
<meta charset="utf-8">
<title>Brindle Mugworks – Retail Coffee Labels</title>
<link href="https://fonts.googleapis.com/css2?family=Archivo:wght@700;800&display=swap" rel="stylesheet">
<style>
  :root{
    --page:#f9e6e7;
    --bag-black:#1d1d1f;
    --seal-black:#0f0f10;
    --bag-kraft:#d6b893;
    --seal-kraft:#c9a983;
    --blend-velvet:#4a66a6;
    --blend-breakfast:#3d8a45;
    --blend-decaf:#a3282c;
    --blend-flavored:#d2b12e;
    --bean-art-light:#4a4a4f;
    --bean-art-dark:#b8966e;
    --ink-light:#e6e6ea;
    --ink-dark:#2a2622;
  }
  *{box-sizing:border-box;margin:0;padding:0}
  html,body{width:1200px;height:543px;overflow:hidden}
  body{background:var(--page);font-family:"Archivo",Arial,sans-serif;position:relative}

  .bag{position:absolute;width:264px;height:500px;overflow:hidden;border-radius:3px;transform-origin:0 0}
  .bag--small{transform:scale(.45)}
  .bag--black{background:var(--bag-black);--seal:var(--seal-black);--art:var(--bean-art-light);--ink:var(--ink-light);--badge:#f2f2f2;--badge-ink:#1d1d1f}
  .bag--kraft{background:var(--bag-kraft);--seal:var(--seal-kraft);--art:var(--bean-art-dark);--ink:var(--ink-dark);--badge:#1d1d1f;--badge-ink:#e6d3b8}

  .bag__seal{position:absolute;left:0;top:0;width:100%;height:44px;background:var(--seal)}
  .bag__beans{position:absolute;left:50px;top:96px;width:64px;height:285px;background:var(--art);opacity:.6;border-radius:32px}
  .bag__band{position:absolute;left:124px;top:91px;width:121px;height:305px;background:var(--band);
    clip-path:polygon(0 0,100% 0,100% 85%,55% 95%,0 100%)}
  .bag__badge{position:absolute;left:101px;top:102px;width:100px;height:100px;border-radius:50%;background:var(--badge);
    display:flex;align-items:center;justify-content:center;text-align:center;
    color:var(--badge-ink);font-weight:800;font-size:13px;line-height:1.1;text-transform:uppercase;padding:10px}
  .bag__name{position:absolute;left:124px;top:292px;width:114px;text-align:right;text-transform:uppercase;font-weight:800;line-height:1.15;font-size:14px}
  .bag__origin{display:block;font-size:15px;color:var(--title);white-space:nowrap}
  .bag__blend{display:block;font-size:10.5px;color:var(--sub);white-space:nowrap}
  .bag__fresh{display:block;font-size:6.5px;color:var(--title);margin-top:3px;white-space:nowrap}
  .bag__weight{position:absolute;right:26px;top:416px;font-size:6.5px;font-weight:700;color:var(--ink);text-transform:uppercase;white-space:nowrap}

  .blend--velvet{--band:var(--blend-velvet);--title:#d3d6df;--sub:#1e2750}
  .blend--breakfast{--band:var(--blend-breakfast);--title:#eef0ee;--sub:#0f2c13}
  .blend--decaf{--band:var(--blend-decaf);--title:#f0e6e6;--sub:#2e0607}
  .blend--flavored{--band:var(--blend-flavored);--title:#fbf6e2;--sub:#1f1a05}
</style>
</head>
<body>
<main class="label-lineup">

  <article class="bag bag--black blend--velvet" style="left:47px;top:30px">
    <div class="bag__seal"></div>
    <div class="bag__beans" role="img" aria-label="Hand-drawn coffee bean column"></div>
    <div class="bag__band"></div>
    <div class="bag__badge">Brindle Mugworks</div>
    <h2 class="bag__name"><span class="bag__origin">Harborline</span><span class="bag__blend">Velvet Blend</span><span class="bag__fresh">Fresh Roasted</span></h2>
    <p class="bag__weight">Net Wt. 10 oz (284g)</p>
  </article>

  <article class="bag bag--kraft blend--velvet" style="left:324px;top:30px">
    <div class="bag__seal"></div>
    <div class="bag__beans" role="img" aria-label="Hand-drawn coffee bean column"></div>
    <div class="bag__band"></div>
    <div class="bag__badge">Brindle Mugworks</div>
    <h2 class="bag__name"><span class="bag__origin">Harborline</span><span class="bag__blend">Velvet Blend</span><span class="bag__fresh">Fresh Roasted</span></h2>
    <p class="bag__weight">Net Wt. 10 oz (284g)</p>
  </article>

  <article class="bag bag--small bag--black blend--breakfast" style="left:636px;top:37px">
    <div class="bag__seal"></div>
    <div class="bag__beans" role="img" aria-label="Hand-drawn coffee bean column"></div>
    <div class="bag__band"></div>
    <div class="bag__badge">Brindle Mugworks</div>
    <h3 class="bag__name"><span class="bag__origin">Colombian</span><span class="bag__blend">Breakfast Blend</span><span class="bag__fresh">Fresh Roasted</span></h3>
    <p class="bag__weight">Net Wt. 10 oz (284g)</p>
  </article>

  <article class="bag bag--small bag--kraft blend--breakfast" style="left:763px;top:37px">
    <div class="bag__seal"></div>
    <div class="bag__beans" role="img" aria-label="Hand-drawn coffee bean column"></div>
    <div class="bag__band"></div>
    <div class="bag__badge">Brindle Mugworks</div>
    <h3 class="bag__name"><span class="bag__origin">Colombian</span><span class="bag__blend">Breakfast Blend</span><span class="bag__fresh">Fresh Roasted</span></h3>
    <p class="bag__weight">Net Wt. 10 oz (284g)</p>
  </article>

  <article class="bag bag--small bag--black blend--decaf" style="left:900px;top:37px">
    <div class="bag__seal"></div>
    <div class="bag__beans" role="img" aria-label="Hand-drawn coffee bean column"></div>
    <div class="bag__band"></div>
    <div class="bag__badge">Brindle Mugworks</div>
    <h3 class="bag__name"><span class="bag__origin">Colombian</span><span class="bag__blend">Decaffeinated</span><span class="bag__fresh">Fresh Roasted</span></h3>
    <p class="bag__weight">Net Wt. 10 oz (284g)</p>
  </article>

  <article class="bag bag--small bag--kraft blend--decaf" style="left:1024px;top:37px">
    <div class="bag__seal"></div>
    <div class="bag__beans" role="img" aria-label="Hand-drawn coffee bean column"></div>
    <div class="bag__band"></div>
    <div class="bag__badge">Brindle Mugworks</div>
    <h3 class="bag__name"><span class="bag__origin">Colombian</span><span class="bag__blend">Decaffeinated</span><span class="bag__fresh">Fresh Roasted</span></h3>
    <p class="bag__weight">Net Wt. 10 oz (284g)</p>
  </article>

  <article class="bag bag--small bag--black blend--flavored" style="left:900px;top:273px">
    <div class="bag__seal"></div>
    <div class="bag__beans" role="img" aria-label="Hand-drawn coffee bean column"></div>
    <div class="bag__band"></div>
    <div class="bag__badge">Brindle Mugworks</div>
    <h3 class="bag__name"><span class="bag__origin">Colombian</span><span class="bag__blend">Flavored Coffee</span><span class="bag__fresh">Fresh Roasted</span></h3>
    <p class="bag__weight">Net Wt. 10 oz (284g)</p>
  </article>

  <article class="bag bag--small bag--kraft blend--flavored" style="left:1024px;top:273px">
    <div class="bag__seal"></div>
    <div class="bag__beans" role="img" aria-label="Hand-drawn coffee bean column"></div>
    <div class="bag__band"></div>
    <div class="bag__badge">Brindle Mugworks</div>
    <h3 class="bag__name"><span class="bag__origin">Colombian</span><span class="bag__blend">Flavored Coffee</span><span class="bag__fresh">Fresh Roasted</span></h3>
    <p class="bag__weight">Net Wt. 10 oz (284g)</p>
  </article>

</main>
</body>
</html>
```